Brantwell Group needs a business card design

We need a new business card design using the logo recently selected in a logo competition on Pixel Forum. Our business is a consultancy specializing in aviation and energy and the winning business card design will promote an image of precision and professionalism with creativity.

Please use the logo with the name on the front of the card and use a complementary font. Make the back white with either the light grey or dark grey logo.

Target Market(s)

Senior finance and legal leaders at aviation and energy companies

Industry/Entity Type

Management Consulting

Contact Information for Business Card

Peter Haldane
President
Brantwell Group

www.brantwellgroup.example

(555) 304-6198
ph@brantwellgroup.example

Requirements
Must have
• Professional font that goes well with the logo font

```html
<!DOCTYPE html>
<html lang="en">
<head>
<meta charset="utf-8">
<title>Brantwell Group – Business Card</title>
<link rel="stylesheet" href="https://fonts.googleapis.com/css2?family=Saira:wght@400;600;700&display=swap">
<style>
  :root {
    --bg-dark: #354340;
    --bg-mid: #5b644f;
    --bg-light: #858a66;
    --accent-blue: #6ec0ec;
    --text-blue: #5aa9dc;
    --navy: #1a2f8f;
    --icon-dark: #111414;
  }
  html, body {
    margin: 0;
    padding: 0;
    overflow: hidden;
    background: #ffffff;
  }
  .card {
    position: relative;
    width: 1200px;
    height: 686px;
    overflow: hidden;
    font-family: "Saira", sans-serif;
    background:
      radial-gradient(ellipse 70% 80% at 68% 62%, var(--bg-light) 0%, var(--bg-mid) 55%, var(--bg-dark) 100%);
  }
  .swoosh {
    position: absolute;
    inset: 0;
    width: 1200px;
    height: 686px;
  }
  .identity {
    position: absolute;
    left: 486px;
    top: 96px;
    color: var(--text-blue);
  }
  .identity__name {
    display: inline-block;
    margin: 0;
    font-weight: 700;
    font-size: 58px;
    line-height: 1;
    letter-spacing: 0.5px;
    text-transform: uppercase;
    padding-bottom: 4px;
    border-bottom: 3px solid var(--text-blue);
  }
  .identity__role,
  .identity__company {
    margin: 0;
    font-weight: 400;
    font-size: 43px;
    line-height: 52px;
  }
  .identity__role { margin-top: 6px; }
  .contact {
    position: absolute;
    left: 50px;
    top: 436px;
    margin: 0;
    padding: 0;
    list-style: none;
  }
  .contact__item {
    display: flex;
    align-items: center;
    height: 38px;
  }
  .contact__icon {
    width: 36px;
    height: 30px;
    margin-right: 10px;
    flex: none;
  }
  .contact__link {
    color: var(--text-blue);
    font-weight: 700;
    font-size: 27px;
    text-transform: uppercase;
    text-decoration: underline;
    text-decoration-thickness: 2px;
    text-underline-offset: 4px;
    letter-spacing: 0.3px;
  }
  .brand {
    position: absolute;
    left: 820px;
    top: 570px;
    width: 340px;
    text-align: center;
    color: var(--navy);
    font-weight: 600;
    font-size: 38px;
    letter-spacing: 1px;
    text-transform: uppercase;
  }
</style>
</head>
<body>
  <div class="card">
    <svg class="swoosh" viewBox="0 0 1200 686" aria-hidden="true">
      <path fill="var(--accent-blue)"
        d="M0,617 C200,636 420,668 640,612 C850,558 960,390 1050,225 C1110,115 1160,78 1200,70
           L1200,128 C1150,150 1120,260 1070,345 C960,525 850,625 600,686 L0,686 Z"/>
    </svg>

    <div class="identity">
      <h1 class="identity__name">Peter Haldane</h1>
      <p class="identity__role">President</p>
      <p class="identity__company">Brantwell Group</p>
    </div>

    <ul class="contact">
      <li class="contact__item">
        <svg class="contact__icon" viewBox="0 0 36 30" aria-hidden="true">
          <rect x="11" y="1" width="16" height="28" rx="3" fill="var(--icon-dark)"/>
          <rect x="14" y="5" width="10" height="17" fill="var(--bg-mid)"/>
          <circle cx="19" cy="25.5" r="1.6" fill="var(--bg-mid)"/>
          <path d="M3,10 C1,14 1,18 3,22 L9,22 L9,10 Z" fill="var(--icon-dark)"/>
        </svg>
        <a class="contact__link" href="tel:5553046198">(555) 304-6198</a>
      </li>
      <li class="contact__item">
        <svg class="contact__icon" viewBox="0 0 36 30" aria-hidden="true">
          <path d="M4,8 L30,6 L28,24 L2,25 Z" fill="var(--accent-blue)"/>
          <path d="M4,8 L16,17 L30,6" fill="none" stroke="#ffffff" stroke-width="2"/>
        </svg>
        <a class="contact__link" href="mailto:ph@brantwellgroup.example">ph@brantwellgroup.example</a>
      </li>
      <li class="contact__item">
        <svg class="contact__icon" viewBox="0 0 36 30" aria-hidden="true">
          <circle cx="16" cy="15" r="12" fill="var(--accent-blue)"/>
          <ellipse cx="16" cy="15" rx="5" ry="12" fill="none" stroke="#ffffff" stroke-width="1.5"/>
          <path d="M4,15 H28 M6,9 H26 M6,21 H26" stroke="#ffffff" stroke-width="1.5"/>
        </svg>
        <a class="contact__link" href="https://www.brantwellgroup.example">www.brantwellgroup.example</a>
      </li>
    </ul>

    <div class="brand">Brantwell Group</div>
  </div>
</body>
</html>
```